Basic Company webpage with the elements and colors of our Logo

Basic Home page with a few pages:
- Home,
- About US,
- Contact us
- Services

Target Market(s)

Business Customers (B2B)

Coding

Coded - Design and coding required

Number of Pages Required

5+ page

Requirements
Must have
• Professional, Clean, Simple High Tech, Contact should have a contact us dialog for sending messages to us
Nice to have
• Meet with us links for calendar access though MS Bookings

```html
<!DOCTYPE html>
<html lang="en">
<head>
<meta charset="utf-8">
<title>Nimbus Tech Group – Innovative IT Solutions</title>
<link rel="stylesheet" href="https://fonts.googleapis.com/css2?family=Libre+Baskerville:wght@700&family=Montserrat:wght@400;500;600;700&display=swap">
<style>
:root{
  --navy:#0b4470;
  --navy-dark:#08355a;
  --orange:#f9a530;
  --ink:#1d2b3a;
  --text:#5f6b78;
  --light:#f3f4f6;
  --white:#ffffff;
  --field:#4d7fa3;
}
*{box-sizing:border-box;margin:0;padding:0}
html,body{width:1200px;height:4841px;overflow:hidden;background:var(--white);font-family:'Montserrat',sans-serif;color:var(--text)}
.page{position:relative;width:1200px;height:4841px;overflow:hidden}
.abs{position:absolute}
.serif{font-family:'Libre Baskerville',serif;font-weight:700;color:var(--navy)}
.photo{position:absolute}
.label{position:absolute;font-size:11px;font-weight:600;color:var(--orange);letter-spacing:.5px;display:flex;align-items:center;gap:14px}
.label::after{content:"";width:50px;height:2px;background:var(--orange)}
.btn{position:absolute;background:var(--orange);color:var(--white);font-weight:600;display:flex;align-items:center;justify-content:center;border-radius:4px}
p.body{font-size:13px;line-height:24px}

/* header */
.topstrip{left:0;top:0;width:1200px;height:34px;background:var(--light)}
.nav{left:0;top:34px;width:1200px;height:52px;background:var(--white)}
.logo{display:flex;align-items:center;gap:8px;font-weight:700;color:var(--navy);font-size:20px}
.logo i{width:14px;height:14px;border-radius:50%;background:var(--orange);display:block}
.menu a{position:absolute;top:56px;font-size:12px;font-weight:500;color:var(--ink);text-decoration:none}
.callbox{left:849px;top:0;width:208px;height:86px;background:var(--navy);color:var(--white);display:flex;align-items:center;gap:12px;padding-left:12px}
.callbox .ring{width:38px;height:38px;border-radius:50%;border:2px solid var(--white);display:flex;align-items:center;justify-content:center}

/* hero */
.hero-card{left:77px;top:272px;width:503px;height:359px;background:var(--white);padding:58px 0 0 45px}
.hero-card::before{content:"";position:absolute;left:0;top:58px;width:4px;height:120px;background:var(--orange)}
.hero-card h1{font-size:50px;line-height:66px}

/* features */
.features{left:92px;top:1536px;width:1010px;height:209px;background:var(--white);border-radius:0 0 90px 90px;box-shadow:0 10px 30px rgba(0,0,0,.08);display:flex;padding:38px 0 0 55px}
.feat{width:310px;display:flex;gap:16px}
.feat .ic{width:62px;height:62px;border-radius:50%;border:2px solid var(--navy);flex:none;display:flex;align-items:center;justify-content:center}
.feat h3{font-family:'Libre Baskerville',serif;color:var(--navy);font-size:21px}
.feat h4{font-size:15px;color:var(--navy);font-weight:500;margin:6px 0 12px}
.feat p{font-size:12px;line-height:24px;color:var(--ink)}

/* services */
.svc-text{position:absolute;width:271px;height:199px;background:var(--white);padding:28px 30px;box-shadow:0 4px 14px rgba(0,0,0,.06)}
.svc-text h3{font-family:'Libre Baskerville',serif;font-size:19px;color:var(--navy)}
.svc-text p{font-size:12px;line-height:24px;margin:14px 0 12px}
.svc-text a{font-size:14px;font-weight:700;color:var(--orange);text-decoration:none}
.svc-text.active{background:var(--navy)}
.svc-text.active h3,.svc-text.active p,.svc-text.active a{color:var(--white)}
.arrow{position:absolute;width:44px;height:60px;background:var(--white);border:1px solid #ddd;display:flex;align-items:center;justify-content:center}

/* why */
.why-item{position:absolute;width:260px;display:flex;gap:14px}
.why-item h4{font-size:15px;font-weight:600;color:var(--navy);margin-bottom:8px}
.why-item p{font-size:12.5px;line-height:24px}
.photo-ring{position:absolute;left:636px;top:2608px;width:474px;height:474px;border-radius:50%;border:9px solid var(--orange);border-left-color:transparent;border-bottom-color:transparent;transform:rotate(12deg)}

/* testimonials */
.tcard{position:absolute;width:321px;height:263px;background:var(--white);text-align:center;padding-top:66px}
.stars{color:#f1632a;font-size:20px;letter-spacing:8px}
.tcard p{font-size:12.5px;line-height:24px;padding:22px 40px 0}
.avatar{position:absolute;width:68px;height:68px;border-radius:50%;background:linear-gradient(#8a96a4,#3b4654)}
.qbadge{position:absolute;width:70px;height:40px;background:var(--navy);border-radius:35px 35px 0 0;color:var(--white);font-family:'Libre Baskerville',serif;font-size:30px;text-align:center;line-height:46px}
.tname{position:absolute;width:321px;text-align:center}
.tname b{display:block;font-size:18px;font-weight:600;color:#3b4654}
.tname span{font-size:13px;color:#8a929c;font-family:'Libre Baskerville',serif;font-weight:400}

/* contact */
.form{left:650px;top:3981px;width:460px;height:470px;background:var(--navy);border:5px solid var(--white);border-radius:18px;text-align:center;color:var(--white)}
.form h2{font-size:27px;font-weight:600;margin-top:36px}
.form p{font-size:11px;line-height:18px;padding:12px 60px 0}
.field{position:absolute;left:29px;width:394px;height:45px;background:var(--field);border-radius:4px;font-size:10px;text-align:left;padding:17px 0 0 26px}
.send{position:absolute;left:29px;top:382px;width:394px;height:44px;background:var(--white);border-radius:4px}

/* footer */
.fcol h5{font-size:14px;font-weight:600;color:var(--navy);padding-bottom:12px;border-bottom:1px solid #cfd6dd;min-width:120px;white-space:nowrap;display:inline-block}
.fcol li{list-style:none;font-size:14px;line-height:32px;color:var(--text)}
.crow{display:flex;gap:14px;font-size:14px;line-height:22px;margin-bottom:12px;color:var(--text)}
.soc{width:26px;height:26px;border-radius:50%;background:#e6e9ee;display:inline-block}
</style>
</head>
<body>
<div class="page">

<!-- header -->
<div class="abs topstrip"></div>
<div class="abs nav"></div>
<div class="abs logo" style="left:104px;top:46px"><i></i>Nimbus Tech</div>
<div class="abs" style="left:393px;top:10px;font-size:12px;font-weight:500;color:var(--ink)">WELCOME</div>
<div class="abs" style="left:624px;top:4px;display:flex;align-items:center;gap:8px;font-size:12px;color:var(--ink)">
  <svg width="26" height="26" viewBox="0 0 26 26"><circle cx="13" cy="13" r="12" fill="none" stroke="#0b4470" stroke-width="1.5"/><rect x="7" y="9" width="12" height="8" fill="none" stroke="#0b4470" stroke-width="1.5"/><path d="M7 9l6 5 6-5" fill="none" stroke="#0b4470" stroke-width="1.5"/></svg>
  info@nimbustech.example
</div>
<nav class="menu">
  <a style="left:336px;color:var(--orange);font-weight:600">HOME</a>
  <a style="left:423px">About Us</a>
  <a style="left:517px">Services</a>
  <a style="left:610px">Gallery</a>
  <a style="left:710px">Contact Us</a>
</nav>
<div class="abs callbox">
  <div class="ring"><svg width="18" height="18" viewBox="0 0 24 24"><path d="M6.6 10.8a15 15 0 006.6 6.6l2.2-2.2a1 1 0 011-.25 11.4 11.4 0 003.6.57 1 1 0 011 1V20a1 1 0 01-1 1A17 17 0 013 4a1 1 0 011-1h3.5a1 1 0 011 1c0 1.25.2 2.45.57 3.6a1 1 0 01-.25 1z" fill="#fff"/></svg></div>
  <div><div style="font-size:13px">Call us today at</div><div style="font-size:19px;font-weight:600;margin-top:4px">(555) 010-2030</div></div>
</div>

<!-- hero -->
<div class="photo" role="img" aria-label="Team meeting in a modern office" style="left:0;top:86px;width:1200px;height:790px;background:linear-gradient(100deg,#1c2a3a 0%,#34495c 45%,#5b6b78 70%,#2a3846 100%)"></div>
<svg class="abs" style="left:0;top:770px" width="1200" height="110" viewBox="0 0 1200 110">
  <path d="M0 40 Q600 110 1200 20 L1200 110 L0 110Z" fill="#fff"/>
</svg>
<div class="abs hero-card">
  <h1 class="serif">Innovative IT<br>Solutions</h1>
  <p class="body" style="font-size:12px;line-height:21px;margin-top:20px;width:410px">orem ipsum dolor sit amet, consectetur adipiscing elit, sed do eiusmo d tempor incididunt ut labore et dolore orem ipsum dolor</p>
</div>
<div class="btn" style="left:124px;top:543px;width:133px;height:37px;font-size:10px;border-radius:0">Discover More</div>

<!-- about -->
<div class="photo" role="img" aria-label="Man in glasses working at a laptop" style="left:103px;top:971px;width:305px;height:315px;border-radius:90px 0 0 0;background:linear-gradient(135deg,#6a7c8c,#c9d2da)"></div>
<div class="photo" role="img" aria-label="Colleagues looking at a screen" style="left:430px;top:994px;width:120px;height:120px;border-radius:0 0 0 40px;background:linear-gradient(135deg,#aab7c2,#e0e6ea)"></div>
<div class="photo" role="img" aria-label="Business partners reviewing a document" style="left:268px;top:1133px;width:303px;height:313px;border-radius:150px 0 90px 0;background:linear-gradient(135deg,#44505e,#b9c2cb)"></div>
<div class="abs" style="left:240px;top:1215px;width:98px;height:98px;border-radius:50%;background:var(--navy)"></div>
<div class="label" style="left:624px;top:991px">ABOUT US</div>
<h2 class="abs serif" style="left:622px;top:1029px;font-size:38px;line-height:60px">Innovative IT Solutions<br>for Development</h2>
<p class="abs body" style="left:624px;top:1157px;width:450px;font-size:12.5px">Lorem ipsum dolor sit amet, consectetur adipiscing elit, sed do eiusmo empor incididunt ut abore et dolore magna aliqua. Ut enim ad minim iam, quis nostrud exercitation ullamco</p>
<p class="abs body" style="left:624px;top:1238px;width:450px;font-size:12.5px">Lorem ipsum dolor sit amet, consectetur adipiscing elit, sed do eiusmo empor incididunt ut abore et dolore magna aliqua. Ut enim ad minim iam, quis nostrud exercitation ullamco</p>
<div class="btn" style="left:625px;top:1345px;width:168px;height:47px;font-size:13px">Contact Us</div>

<div class="abs features">
  <div class="feat"><div class="ic"><svg width="30" height="30" viewBox="0 0 30 30"><circle cx="15" cy="15" r="5" fill="none" stroke="#0b4470" stroke-width="2"/><circle cx="15" cy="15" r="10" fill="none" stroke="#0b4470" stroke-width="2" stroke-dasharray="4 3"/></svg></div>
    <div><h3>Expertise</h3><h4>Lorem Ipsum</h4><p>Lorem ipsum dolor sit amet,<br>empor incididunt ut abore et<br>iam, quis nostrud exe</p></div></div>
  <div class="feat"><div class="ic"><svg width="30" height="30" viewBox="0 0 30 30"><circle cx="13" cy="13" r="9" fill="none" stroke="#0b4470" stroke-width="2"/><circle cx="20" cy="20" r="5" fill="none" stroke="#0b4470" stroke-width="2"/></svg></div>
    <div><h3>Professional</h3><h4>Lorem Ipsum</h4><p>Lorem ipsum dolor sit amet,<br>empor incididunt ut abore et<br>iam, quis nostrud exe</p></div></div>
  <div class="feat"><div class="ic"><svg width="30" height="30" viewBox="0 0 30 30"><circle cx="15" cy="10" r="5" fill="none" stroke="#0b4470" stroke-width="2"/><path d="M5 26c0-6 4-9 10-9s10 3 10 9z" fill="none" stroke="#0b4470" stroke-width="2"/></svg></div>
    <div><h3>Experienced</h3><h4>Lorem Ipsum</h4><p>Lorem ipsum dolor sit amet,<br>empor incididunt ut abore et<br>iam, quis nostrud exe</p></div></div>
</div>

<!-- services -->
<div class="abs" style="left:0;top:1784px;width:1200px;height:723px;background:var(--light)"></div>
<div class="label" style="left:94px;top:1853px">BENEFITS</div>
<h2 class="abs serif" style="left:93px;top:1893px;font-size:38px">Services We <span style="color:var(--orange)">Provide</span></h2>
<div class="arrow" style="left:1005px;top:1870px"><svg width="12" height="16"><path d="M9 2L3 8l6 6" fill="none" stroke="#1d2b3a" stroke-width="2"/></svg></div>
<div class="arrow" style="left:1058px;top:1870px"><svg width="12" height="16"><path d="M3 2l6 6-6 6" fill="none" stroke="#1d2b3a" stroke-width="2"/></svg></div>

<div class="photo" role="img" aria-label="Two businessmen in discussion" style="left:90px;top:1974px;width:321px;height:235px;background:linear-gradient(135deg,#5d6a78,#d8dee3)"></div>
<div class="photo" role="img" aria-label="Woman in a black top in an office" style="left:438px;top:1974px;width:321px;height:235px;background:linear-gradient(135deg,#b4bec7,#eef1f3)"></div>
<div class="photo" role="img" aria-label="Colleagues gathered around a laptop" style="left:785px;top:1974px;width:321px;height:235px;background:linear-gradient(135deg,#6d7986,#c4ccd3)"></div>
<div class="svc-text" style="left:120px;top:2150px"><h3>IT Procurement</h3><p>Lorem ipsum dolor sit amet, con sectetur Lorem ipsum dolor sit am et, consectetur Lorem ipsum dolor</p><a>Read More</a></div>
<div class="svc-text active" style="left:459px;top:2150px"><h3>Cloud Services</h3><p>Lorem ipsum dolor sit amet, con sectetur Lorem ipsum dolor sit am et, consectetur Lorem ipsum dolor</p><a>Read More</a></div>
<div class="svc-text" style="left:805px;top:2150px"><h3>Cyber Security</h3><p>Lorem ipsum dolor sit amet, con sectetur Lorem ipsum dolor sit am et, consectetur Lorem ipsum dolor</p><a>Read More</a></div>
<div class="abs" style="left:500px;top:2391px;width:191px;height:45px;border:2px solid var(--navy);border-radius:23px;color:var(--navy);font-size:13px;font-weight:600;display:flex;align-items:center;justify-content:center">MORE SERVICES</div>

<!-- why choose -->
<div class="label" style="left:94px;top:2610px">WHY CHOOSE US</div>
<h2 class="abs serif" style="left:92px;top:2645px;font-size:38px;line-height:60px">IT Solutions for<br>Your Next Big Project</h2>
<p class="abs body" style="left:94px;top:2777px;width:470px;font-size:12.5px">Lorem ipsum dolor sit amet, consectetur adipiscing elit, sed do eiusmo empor incididunt ut abore et dolore magna aliqua. Ut enim ad minim iam, quis nostrud exercitation ullamco</p>
<div class="why-item" style="left:108px;top:2877px"><svg width="30" height="30" viewBox="0 0 30 30"><path d="M5 18a10 10 0 0120 0" fill="none" stroke="#0b4470" stroke-width="2"/><path d="M15 12v12M11 20l4 4 4-4" fill="none" stroke="#0b4470" stroke-width="2"/></svg><div><h4>Quality Services</h4><p>Lorem ipsum dolor sit amet, consectetur adipiscing</p></div></div>
<div class="why-item" style="left:373px;top:2877px"><svg width="30" height="30" viewBox="0 0 30 30"><path d="M15 3l4 8 9 1-7 6 2 9-8-5-8 5 2-9-7-6 9-1z" fill="none" stroke="#0b4470" stroke-width="2"/></svg><div><h4>Proven Record</h4><p>Lorem ipsum dolor sit amet, consectetur adipiscing</p></div></div>
<div class="why-item" style="left:108px;top:2973px"><svg width="30" height="30" viewBox="0 0 30 30"><path d="M4 26h22M9 22l10-18 4 2-10 18z" fill="none" stroke="#0b4470" stroke-width="2"/></svg><div><h4>Trusted Professionals</h4><p>Lorem ipsum dolor sit amet, consectetur adipiscing</p></div></div>
<div class="why-item" style="left:373px;top:2973px"><svg width="30" height="30" viewBox="0 0 30 30"><circle cx="10" cy="9" r="4" fill="none" stroke="#0b4470" stroke-width="2"/><circle cx="21" cy="9" r="4" fill="none" stroke="#0b4470" stroke-width="2"/><path d="M3 24c0-5 3-8 7-8s7 3 7 8M14 24c0-5 3-8 7-8s7 3 7 8" fill="none" stroke="#0b4470" stroke-width="2"/></svg><div><h4>Client Centric</h4><p>Lorem ipsum dolor sit amet, consectetur adipiscing</p></div></div>
<div class="photo-ring"></div>
<div class="photo" role="img" aria-label="Smiling professional woman in an office" style="left:649px;top:2624px;width:448px;height:448px;border-radius:50%;background:linear-gradient(135deg,#cfc6ba,#8f8578)"></div>

<!-- testimonials -->
<div class="abs" style="left:0;top:3161px;width:1200px;height:736px;background:var(--light)"></div>
<div class="label" style="left:497px;top:3222px"><span style="width:50px;height:2px;background:var(--orange);display:block"></span>TESTIMONIALS</div>
<h2 class="abs serif" style="left:0;top:3262px;width:1200px;text-align:center;font-size:38px">What Clients are <span style="color:var(--orange)">Saying</span></h2>
<div class="tcard" style="left:90px;top:3390px"><div class="stars">★★★★★</div><p>Lorem ipsum dolor sit amet, consectetur adipiscing elit, sed do eiusmod tempor incididunt ut labore et dolore</p></div>
<div class="tcard" style="left:439px;top:3390px"><div class="stars">★★★★★</div><p>Lorem ipsum dolor sit amet, consectetur adipiscing elit, sed do eiusmod tempor incididunt ut labore et dolore</p></div>
<div class="tcard" style="left:786px;top:3390px"><div class="stars">★★★★★</div><p>Lorem ipsum dolor sit amet, consectetur adipiscing elit, sed do eiusmod tempor incididunt ut labore et dolore</p></div>
<div class="avatar" role="img" aria-label="Client portrait" style="left:217px;top:3356px"></div>
<div class="avatar" role="img" aria-label="Client portrait" style="left:566px;top:3356px"></div>
<div class="avatar" role="img" aria-label="Client portrait" style="left:913px;top:3356px"></div>
<div class="qbadge" style="left:216px;top:3613px">“</div>
<div class="qbadge" style="left:565px;top:3613px">“</div>
<div class="qbadge" style="left:912px;top:3613px">“</div>
<div class="tname" style="left:90px;top:3686px"><b>Dana Whitfield</b><span>Country</span></div>
<div class="tname" style="left:439px;top:3686px"><b>Dana Whitfield</b><span>Country</span></div>
<div class="tname" style="left:786px;top:3686px"><b>Dana Whitfield</b><span>Country</span></div>

<!-- contact -->
<div class="photo" role="img" aria-label="Seaside terrace with a calm sea" style="left:0;top:3897px;width:1200px;height:501px;background:linear-gradient(180deg,#9aa8b3,#4f6778 60%,#2f4b5e)"></div>
<div class="photo" role="img" aria-label="Woman in a white blouse using a tablet" style="left:180px;top:3775px;width:330px;height:623px;border-radius:160px 160px 0 0;background:linear-gradient(180deg,#e9e5df,#c9b59a)"></div>
<div class="abs form">
  <h2>Connect With Us</h2>
  <p>Lorem ipsum dolor sit amet, consectetur adipiscing elit, sed do eius mod tempor incididunt ut labore et...</p>
  <div class="field" style="top:132px">NAME</div>
  <div class="field" style="top:207px">E-MAIL</div>
  <div class="field" style="top:281px">MESSAGE</div>
  <div class="send"></div>
</div>

<!-- footer -->
<div class="abs logo" style="left:104px;top:4604px"><i></i>Nimbus Tech</div>
<div class="abs" style="left:113px;top:4672px;display:flex;align-items:center;gap:10px;font-size:14px;color:var(--ink)">Follow Us <span class="soc"></span><span class="soc"></span><span class="soc"></span></div>
<div class="abs fcol" style="left:364px;top:4555px"><h5>Quick Links</h5><ul style="margin-top:12px"><li>Home</li><li>About us</li><li>Services</li><li>Contact us</li></ul></div>
<div class="abs fcol" style="left:586px;top:4555px"><h5>Contact</h5>
  <div style="margin-top:22px">
    <div class="crow"><svg width="16" height="20" viewBox="0 0 16 20"><path d="M8 19s6-7 6-11A6 6 0 002 8c0 4 6 11 6 11z" fill="none" stroke="#f9a530" stroke-width="1.5"/><circle cx="8" cy="8" r="2" fill="#f9a530"/></svg><span>1234 Location<br>1456 Street</span></div>
    <div class="crow"><svg width="16" height="16" viewBox="0 0 24 24"><path d="M6.6 10.8a15 15 0 006.6 6.6l2.2-2.2a1 1 0 011-.25 11.4 11.4 0 003.6.57 1 1 0 011 1V20a1 1 0 01-1 1A17 17 0 013 4a1 1 0 011-1h3.5a1 1 0 011 1c0 1.25.2 2.45.57 3.6a1 1 0 01-.25 1z" fill="none" stroke="#f9a530" stroke-width="1.8"/></svg><span>1-800-555-0142</span></div>
    <div class="crow"><svg width="16" height="14" viewBox="0 0 16 14"><rect x="1" y="2" width="14" height="10" fill="none" stroke="#f9a530" stroke-width="1.5"/><path d="M1 2l7 6 7-6" fill="none" stroke="#f9a530" stroke-width="1.5"/></svg><span>info@nimbustech.example</span></div>
  </div></div>
<div class="abs fcol" style="left:860px;top:4555px"><h5>Join our Newsletter</h5>
  <p style="font-size:14px;line-height:18px;margin-top:22px;width:230px">Sign up for our newsletter to know the latest from us</p>
  <div style="display:flex;margin-top:14px"><div style="width:145px;height:32px;border:1px solid #cfd6dd;font-size:12px;padding:8px 0 0 18px;color:#8a929c">Email</div><div style="width:100px;height:32px;background:var(--orange);color:#fff;font-size:12px;font-weight:700;display:flex;align-items:center;justify-content:center">SUBSCRIBE</div></div>
</div>
<div class="abs" style="left:113px;top:4770px;width:975px;height:1px;background:#dde2e7"></div>
<div class="abs" style="left:0;top:4796px;width:1200px;text-align:center;font-size:12px;font-weight:500;color:var(--navy)">Nimbus Tech Group</div>

</div>
</body>
</html>
```